Ridgemoor Partners

Need a new website - see more on ridgemoorpartners.com

Target Market(s)

Finance industry = conservative design

Coding

Coded - Design and coding required

Number of Pages Required

5+ page

Requirements
Should not have
• Dear all,
• Please avoid pictures of people on the website (except the "team" of course :-)

```html
<!DOCTYPE html>
<html lang="en">
<head>
<meta charset="utf-8">
<title>Ridgemoor Partners</title>
<link rel="stylesheet" href="https://fonts.googleapis.com/css2?family=Open+Sans:wght@300;400;600;700&display=swap">
<style>
:root{
  --ink:#1f1f1f;
  --text:#333333;
  --muted:#555555;
  --white:#ffffff;
  --black:#000000;
  --hero-red:#e8230f;
  --band-blue:#86a8f7;
  --social-blue:#2b8fd6;
  --coral:#f18275;
  --office-dark:#2e2624;
  --footer:#1c1c1e;
  --icon-blue:#4a90d9;
  --icon-red:#e8412f;
  --icon-purple:#7b5cf0;
}
*{margin:0;padding:0;box-sizing:border-box}
html,body{width:1200px;height:3383px;overflow:hidden}
body{position:relative;background:var(--white);font-family:"Open Sans",Arial,sans-serif;color:var(--text)}
.abs{position:absolute}
.center{text-align:center}

/* header */
.site-header{left:0;top:0;width:1200px;height:68px;background:var(--white)}
.brand{left:112px;top:20px;display:flex;align-items:center;gap:8px;font-size:13px;font-weight:600;color:var(--ink)}
.brand-dot{width:26px;height:26px;border-radius:50%;background:#2a5fc8}
.main-nav{left:562px;top:26px;display:flex;gap:0;font-size:12px;color:var(--ink)}
.main-nav span{margin-right:30px}
.main-nav .active{color:#3a6ad6}
.search-icon{left:1073px;top:26px}

/* hero */
.hero{left:0;top:68px;width:1200px;height:451px;background:var(--black)}
.hero-title{left:0;top:238px;width:1200px;font-size:33px;font-weight:300;line-height:54px;color:var(--white)}
.hero-rule{left:469px;top:372px;width:264px;height:2px;background:var(--white)}
.hero-arrow{left:559px;top:388px}

/* section headings */
.section-title{left:0;width:1200px;font-size:32px;font-weight:400;color:var(--ink);letter-spacing:1px}
.section-rule{left:550px;width:100px;height:2px;background:#666}
.section-lead{left:90px;width:1020px;font-size:12.5px;line-height:20px;color:var(--muted)}

/* services */
.service{width:320px;text-align:center}
.service-icon{display:block;margin:0 auto 22px}
.service h3{font-size:17px;font-weight:400;color:var(--ink);line-height:22px;margin-bottom:10px}
.service p{font-size:12.5px;line-height:19px;color:var(--muted);padding:0 18px}

/* partners band */
.partners-band{left:0;top:1067px;width:1200px;height:490px;background:var(--band-blue)}
.partners-title{left:0;top:1212px;width:1200px;font-size:29px;color:#2a2a2a}
.partners-lead{left:90px;top:1296px;width:1020px;font-size:12.5px;line-height:20px;color:#3a3a3a}
.partner-row{left:250px;top:1412px;width:700px;display:flex;justify-content:space-between;align-items:center;font-size:40px;font-weight:600;color:var(--ink)}

/* team */
.member{width:470px;text-align:center}
.photo{width:176px;height:248px;margin:0 auto;background:linear-gradient(160deg,#8b6c62,#4a3b38 60%,#2b2322)}
.photo.alt{background:linear-gradient(160deg,#c9c4bb,#6f6b66 55%,#2f3a4c)}
.member h4{margin-top:32px;font-size:16px;font-weight:700;color:var(--ink)}
.member .name-rule{width:50px;height:2px;background:var(--ink);margin:8px auto 8px}
.member .role{font-size:12.5px;color:var(--text)}
.member p{margin-top:10px;font-size:12.5px;line-height:21px;color:var(--text)}
.social{display:flex;justify-content:center;gap:8px;margin-top:14px}
.social span{width:29px;height:29px;background:var(--social-blue)}

/* office */
.office-band{left:0;top:2719px;width:1200px;height:304px}
.office-photo{left:108px;top:2734px;width:483px;height:276px;border-radius:0 90px 0 90px;background:linear-gradient(180deg,#4a4d52 0%,#7b7d80 45%,#b9b3a8 100%)}
.office-title{left:819px;top:2748px;font-size:27px;font-weight:400;color:var(--white)}
.office-text{left:819px;top:2789px;width:300px;font-size:12.5px;line-height:20px;color:var(--white)}
.office-text p{margin-bottom:8px}

/* footer */
.site-footer{left:0;top:3046px;width:1200px;height:337px;background:var(--footer);color:var(--white)}
.footer-col{top:3120px}
.footer-col h5{font-size:19px;font-weight:400;margin-bottom:14px}
.footer-col li{list-style:none;font-size:12.5px;font-weight:700;line-height:27px}
.footer-icons{display:flex;gap:10px;margin-top:14px}
.footer-icons span{width:13px;height:13px;background:var(--white)}
.credits{left:92px;top:3300px;font-size:12px;color:#d0d0d0}
.to-top{left:1152px;top:3354px;width:30px;height:29px;border:1px solid #555}
</style>
</head>
<body>

<header class="site-header abs">
  <div class="brand abs"><span class="brand-dot"></span>Ridgemoor Partners</div>
  <nav class="main-nav abs">
    <span>HOME</span><span class="active">SERVICES</span><span>CURRENT ENGAGEMENTS</span><span>NEWS</span><span>TEAM</span><span>CONTACT</span>
  </nav>
  <svg class="search-icon abs" width="14" height="14" viewBox="0 0 14 14"><circle cx="5.5" cy="5.5" r="4" fill="none" stroke="#2a4fc0" stroke-width="2"/><line x1="8.5" y1="8.5" x2="13" y2="13" stroke="#2a4fc0" stroke-width="2"/></svg>
</header>

<section class="hero abs"></section>
<h1 class="hero-title abs center">Ridgemoor Partners is a privately held global<br>investment holding group</h1>
<div class="hero-rule abs"></div>
<svg class="hero-arrow abs" width="84" height="70" viewBox="0 0 84 70"><polygon points="42,0 84,70 0,70" fill="var(--hero-red)"/></svg>

<h2 class="section-title abs center" style="top:645px">OUR SERVICES</h2>
<div class="section-rule abs" style="top:706px"></div>
<p class="section-lead abs center" style="top:726px">We offer a wide range of financial services to privately held and publicly-traded companies in the United States, Europe and Asia. Though not limited to, Ridgemoor focuses on the luxury goods sector, primarily taking companies within the high-end consumer industries public, as well as financing already listed companies.</p>

<div class="service abs" style="left:110px;top:830px">
  <svg class="service-icon" width="64" height="50" viewBox="0 0 64 50"><rect x="2" y="2" width="60" height="46" fill="none" stroke="var(--icon-blue)" stroke-width="2"/><rect x="22" y="10" width="20" height="30" fill="none" stroke="var(--icon-blue)" stroke-width="2"/><line x1="12" y1="25" x2="52" y2="25" stroke="var(--icon-blue)" stroke-width="2"/></svg>
  <h3>Private Placements</h3>
  <p>Ridgemoor Partners efficiently arranges both equity and debt financing by offering new capital to public and private companies.</p>
</div>
<div class="service abs" style="left:440px;top:830px">
  <svg class="service-icon" width="50" height="50" viewBox="0 0 50 50"><line x1="25" y1="4" x2="25" y2="48" stroke="var(--icon-red)" stroke-width="2"/><polygon points="8,8 40,8 46,14 40,20 8,20" fill="none" stroke="var(--icon-red)" stroke-width="2"/><polygon points="42,24 10,24 4,30 10,36 42,36" fill="none" stroke="var(--icon-red)" stroke-width="2"/></svg>
  <h3>Reverse Mergers &amp; Alternative<br>Offerings</h3>
  <p>Ridgemoor Partners assists fast growing privately-held companies with easy and affordable access to the public markets in the U.S.</p>
</div>
<div class="service abs" style="left:770px;top:830px">
  <svg class="service-icon" width="54" height="50" viewBox="0 0 54 50"><polygon points="27,4 50,16 27,28 4,16" fill="none" stroke="var(--icon-purple)" stroke-width="2"/><polyline points="4,25 27,37 50,25" fill="none" stroke="var(--icon-purple)" stroke-width="2"/><polyline points="4,34 27,46 50,34" fill="none" stroke="var(--icon-purple)" stroke-width="2"/></svg>
  <h3>Mergers &amp; Acquisitions</h3>
  <p>Nemo enim ipsam voluptatem quia voluptas sit aspernatur aut odit aut fugit, sed quia consequuntur magni dolores eos qui ratione voluptatem sequi nesciunt.</p>
</div>

<section class="partners-band abs"></section>
<h2 class="partners-title abs center">Ridgemoor Partners</h2>
<p class="partners-lead abs center">Sed ut perspiciatis unde omnis iste natus error sit voluptatem accusantium doloremque laudantium, totam rem aperiam, eaque ipsa quae ab illo inventore veritatis et quasi architecto beatae vitae dicta sunt explicabo.</p>
<div class="partner-row abs"><span>Sparkline</span><span>Norrvik</span><span>Brightmind</span></div>

<h2 class="section-title abs center" style="top:1598px;font-size:29px;letter-spacing:0">Ridgemoor Core Team</h2>
<p class="section-lead abs center" style="top:1662px">Sed ut perspiciatis unde omnis iste natus error sit voluptatem accusantium doloremque laudantium, totam rem aperiam, eaque ipsa quae ab illo inventore veritatis et quasi architecto beatae vitae dicta sunt explicabo.</p>

<div class="member abs" style="left:122px;top:1726px">
  <div class="photo" role="img" aria-label="Portrait photo of the managing director"></div>
  <h4>Anders Vallin</h4>
  <div class="name-rule"></div>
  <div class="role">Managing Director</div>
  <p>Mr. Vallin, an international financier, has over 25 years experience in the global financial services industry as a securities professional. From 1996 through 2003, Mr. Vallin was Co-Founder and Managing Partner of Harbor Crest Capital in London, in charge of the private placement division of the company. From 1991 through 1996, Mr. Vallin was Senior Portfolio Manager of Kestrel Fund Managers, a London-based hedge fund. Mr. Vallin started his career in 1986 with Nordhavn Bank in Copenhagen, Denmark. In early 2004, Mr. Vallin launched a new investment holding company, Ridgemoor Partners, serving as Managing Director and overseeing the company's overall investments, investment banking practice, including origination, structuring and financing of both privately-held and publicly traded emerging growth companies in North America, Asia and Europe.</p>
  <div class="social"><span></span><span></span><span></span><span></span></div>
</div>

<div class="member abs" style="left:618px;top:1726px">
  <div class="photo alt" role="img" aria-label="Portrait photo of the managing partner"></div>
  <h4>Mikkel Strand</h4>
  <div class="name-rule"></div>
  <div class="role">Managing Partner</div>
  <p>Mr. Strand has an impressive resume as a stock broker and equity portfolio manager with a widespread aspect of highly acknowledged investment funds. After working within this segment of finance for roughly 13 years, he advanced into performing reverse mergers, PPMs and IPOs in the US, making him a strong profile within the transatlantic investment arena as well as an esteemed real estate investor. Since 2010, Mr. Strand has served as a trusted introducer between highly acknowledged investment organizations and private high net worth individuals. Thus he brings an unprecedented network of both private and institutional investors to the Ridgemoor family.</p>
  <div class="social"><span></span><span></span><span></span><span></span></div>
</div>

<h2 class="section-title abs center" style="top:2505px">CONTACT US</h2>
<div class="section-rule abs" style="top:2565px"></div>
<p class="section-lead abs center" style="top:2592px">Sed ut perspiciatis unde omnis iste natus error sit voluptatem accusantium doloremque laudantium, totam rem aperiam, eaque ipsa quae ab illo inventore veritatis et quasi architecto beatae vitae dicta sunt explicabo.</p>

<svg class="office-band abs" width="1200" height="304" viewBox="0 0 1200 304"><rect width="1200" height="304" fill="var(--coral)"/><polygon points="823,0 1200,0 1200,304 704,304" fill="var(--office-dark)"/></svg>
<div class="office-photo abs" role="img" aria-label="Photo of a modern office corridor with reception desk"></div>
<h3 class="office-title abs">OUR OFFICE</h3>
<div class="office-text abs">
  <p>Founded in 2004.</p>
  <p>Ridgemoor is headquartered in Gibraltar with representative offices in Luxembourg and London.</p>
</div>

<footer class="site-footer abs"></footer>
<div class="footer-col abs" style="left:92px;color:#fff">
  <h5>Ridgemoor Partners</h5>
  <ul><li>Sparkline Blockchain Company</li><li>Brightmind Involvement Marketing</li><li>Norrvik</li></ul>
</div>
<div class="footer-col abs" style="left:354px;color:#fff">
  <h5>Services</h5>
  <ul><li>Private Placements</li><li style="line-height:19px;padding:4px 0">Reverse Mergers &amp; Alternative<br>Offerings</li><li>Mergers &amp; Acquisitions</li></ul>
</div>
<div class="footer-col abs" style="left:614px;color:#fff">
  <h5>Follow us</h5>
  <div class="footer-icons"><span></span><span></span></div>
</div>
<div class="credits abs">Theme by Linework Powered by PressKit</div>
<div class="to-top abs"></div>

</body>
</html>
```